Refresh of Business Card Design

Want to refresh the business card design with the new logo while adhering to style guide as attached. Would like to match feel of website www.durmackvinex.com

```html
<!DOCTYPE html>
<html lang="en">
<head>
<meta charset="utf-8">
<title>Durmack Vinex – Business Card</title>
<link href="https://fonts.googleapis.com/css2?family=Lato:wght@400;700;900&display=swap" rel="stylesheet">
<style>
  :root{
    --bg:#202020;
    --crimson:#a3173a;
    --red:#e3173f;
    --black:#0c0c0e;
    --white:#ffffff;
    --ink:#1d1d1d;
    --silver:#c9c9cc;
  }
  *{margin:0;padding:0;box-sizing:border-box}
  html,body{width:1200px;height:939px;overflow:hidden}
  body{background:var(--bg);font-family:'Lato',sans-serif;position:relative}

  .card{position:absolute;left:250px;width:700px;height:400px;border-radius:22px;overflow:hidden}
  .card--back{top:40px;background:radial-gradient(ellipse 60% 70% at 50% 42%,var(--crimson) 0%,#5a0c22 55%,var(--black) 100%)}
  .card--front{top:499px;background:var(--white)}

  .brand{display:flex;align-items:center;gap:16px}
  .brand__dot{width:54px;height:54px;border-radius:50%;flex:none}
  .brand__name{font-weight:900;font-size:34px;letter-spacing:2px;text-transform:uppercase}

  .card--back .brand{position:absolute;left:0;right:0;top:150px;justify-content:center}
  .card--back .brand__dot{background:var(--red);border:4px solid var(--silver)}
  .card--back .brand__name{color:var(--white)}
  .back__url{position:absolute;left:0;right:0;bottom:48px;text-align:center;color:var(--white);font-size:19px;letter-spacing:2px}
  .back__url b{font-weight:700}

  .card--front .brand{position:absolute;left:44px;top:170px;flex-direction:column;gap:12px;width:260px}
  .card--front .brand__dot{width:110px;height:110px;background:var(--red);border:6px solid var(--ink)}
  .card--front .brand__name{color:var(--ink);font-size:26px;text-align:center}

  .contact{position:absolute;left:340px;top:96px;width:330px}
  .contact__name{color:var(--red);font-weight:900;font-size:31px;text-transform:uppercase;letter-spacing:.5px}
  .contact__role{color:var(--ink);font-size:18px;margin-top:2px}
  .contact__rule{width:34px;height:2px;background:var(--red);margin:10px 0 14px}
  .contact__list{list-style:none}
  .contact__item{display:flex;align-items:center;gap:12px;font-size:15.5px;color:var(--ink);line-height:1;margin-bottom:11px}
  .contact__item svg{width:14px;height:14px;flex:none;fill:var(--red)}
</style>
</head>
<body>

<section class="card card--back">
  <div class="brand">
    <span class="brand__dot"></span>
    <span class="brand__name">Durmack Vinex</span>
  </div>
  <p class="back__url">WWW.<b>DURMACKVINEX</b>.COM</p>
</section>

<section class="card card--front">
  <div class="brand">
    <span class="brand__dot"></span>
    <span class="brand__name">Durmack Vinex</span>
  </div>

  <div class="contact">
    <h1 class="contact__name">Mara Ellison</h1>
    <p class="contact__role">Sales</p>
    <div class="contact__rule"></div>
    <ul class="contact__list">
      <li class="contact__item">
        <svg viewBox="0 0 14 14"><path d="M4 0h6a1 1 0 0 1 1 1v12a1 1 0 0 1-1 1H4a1 1 0 0 1-1-1V1a1 1 0 0 1 1-1zm.5 1.5v9.5h5V1.5z"/></svg>
        555.014.2290
      </li>
      <li class="contact__item">
        <svg viewBox="0 0 14 14"><path d="M0 3h14v8H0zm1.2 1 5.8 4 5.8-4z"/></svg>
        mellison@durmackvinex.com
      </li>
      <li class="contact__item">
        <svg viewBox="0 0 14 14"><path d="M7 0a7 7 0 1 0 0 14A7 7 0 0 0 7 0zm0 1.3c.8.9 1.5 2.8 1.6 5H5.4C5.5 4.1 6.2 2.2 7 1.3zM1.3 7.7h2.8c.1 1.9.6 3.5 1.3 4.6A5.7 5.7 0 0 1 1.3 7.7zm0-1.4A5.7 5.7 0 0 1 5.4 1.7c-.7 1.1-1.2 2.7-1.3 4.6zm5.7 6.4c-.8-.9-1.5-2.8-1.6-5h3.2c-.1 2.2-.8 4.1-1.6 5zm1.6-.4c.7-1.1 1.2-2.7 1.3-4.6h2.8a5.7 5.7 0 0 1-4.1 4.6zm1.3-6C9.8 4.4 9.3 2.8 8.6 1.7a5.7 5.7 0 0 1 4.1 4.6z"/></svg>
        www.durmackvinex.com
      </li>
      <li class="contact__item">
        <svg viewBox="0 0 14 14"><path d="M7 0a5 5 0 0 0-5 5c0 3.8 5 9 5 9s5-5.2 5-9a5 5 0 0 0-5-5zm0 7a2 2 0 1 1 0-4 2 2 0 0 1 0 4z"/></svg>
        42 Harlow Ridge Rd Kestrel, TX 70421
      </li>
      <li class="contact__item">
        <svg viewBox="0 0 14 14"><path d="M7 0a5 5 0 0 0-5 5c0 3.8 5 9 5 9s5-5.2 5-9a5 5 0 0 0-5-5zm0 7a2 2 0 1 1 0-4 2 2 0 0 1 0 4z"/></svg>
        P.O.Box 20418 Fenwick, TX 70488
      </li>
    </ul>
  </div>
</section>

</body>
</html>
```